FOOD DELIVERY BRAND NEEDS WEBSITE TO GET SUBSCRIBERS

web design needed for a food delivery brand/label,
website should display who we are, how it works and push futur clients to get the label for an online application. Should look serious/official, trustworthy and confident. colors are black and gold like logo

Target Market(s)

restaurants

Industry/Entity Type

restaurant

Number of Pages Required

4 page

Requirements
Must have
• home page, who we are, our partners, subscribe, 2 subscribe button : 1 on top 1 bottom
Nice to have
• a graphic showing average + 15% sales thanks the label

```html
<!DOCTYPE html>
<html lang="en">
<head>
<meta charset="utf-8">
<title>Amber Route — How it Works</title>
<link href="https://fonts.googleapis.com/css2?family=Poppins:wght@600;700&family=Lato:wght@400;700&family=Dancing+Script:wght@600&display=swap" rel="stylesheet">
<style>
  :root {
    --gold: #d4a20a;
    --ink: #1f1f1f;
    --body: #3a3a3a;
    --muted: #9b9ba6;
    --page: #ffffff;
    --rule: #dcdcdc;
  }
  * { box-sizing: border-box; margin: 0; padding: 0; }
  html, body { width: 1200px; height: 638px; overflow: hidden; background: var(--page); }
  body { position: relative; font-family: "Lato", sans-serif; border-top: 1px solid var(--rule); }

  .steps-kicker {
    position: absolute; top: 2px; left: 0; width: 1200px; text-align: center;
    font-family: "Dancing Script", cursive; font-size: 20px; color: var(--gold);
  }
  .steps-title {
    position: absolute; top: 38px; left: 0; width: 1200px; text-align: center;
    font-family: "Poppins", sans-serif; font-weight: 700; font-size: 33px;
    color: var(--ink); letter-spacing: 0.2px;
  }
  .step { position: absolute; top: 112px; width: 300px; text-align: center; }
  .step--one { left: 118px; }
  .step--two { left: 450px; }
  .step--three { left: 782px; }
  .step-icon { position: relative; width: 96px; height: 96px; margin: 0 auto; }
  .step-art { width: 92px; height: 92px; border-radius: 50%; margin: 0 auto; }
  .step--one .step-art { background: linear-gradient(135deg, #ff5a2a 40%, #dcb65f 60%); }
  .step--two .step-art { background: linear-gradient(135deg, #12bfc0 40%, #f3dc9c 60%); }
  .step--three .step-art { background: linear-gradient(135deg, #10d69a 45%, #5a6470 55%); }
  .step-number {
    position: absolute; left: 33px; top: 75px; width: 30px; height: 30px; border-radius: 50%;
    background: var(--gold); color: #fff; font-family: "Poppins", sans-serif; font-weight: 700;
    font-size: 12px; line-height: 30px; text-align: center;
  }
  .step-name {
    margin-top: 20px; font-family: "Poppins", sans-serif; font-weight: 600;
    font-size: 17px; color: var(--ink);
  }
  .step-text { margin-top: 9px; font-size: 12.5px; line-height: 23px; color: var(--muted); }

  .about-title {
    position: absolute; top: 434px; left: 60px; width: 582px; text-align: center;
    font-family: "Poppins", sans-serif; font-weight: 700; font-size: 35px; color: var(--ink);
  }
  .about-tag {
    position: absolute; top: 492px; left: 283px; width: 136px; height: 21px;
    background: var(--gold); clip-path: polygon(4% 0, 100% 0, 96% 100%, 0 100%);
    color: #fff; font-family: "Poppins", sans-serif; font-style: italic; font-weight: 600;
    font-size: 8.5px; letter-spacing: 2.4px; line-height: 21px; text-align: center;
  }
  .about-text {
    position: absolute; top: 539px; left: 112px; width: 478px; text-align: center;
    font-size: 12.5px; line-height: 23px; color: var(--body);
  }

  .photo { position: absolute; border-radius: 3px; box-shadow: 0 10px 30px rgba(0,0,0,0.12); }
  .photo--back { left: 783px; top: 421px; width: 304px; height: 162px;
    background: linear-gradient(120deg, #e9b24a, #b59a7c 55%, #7c6450); }
  .photo--low { left: 610px; top: 605px; width: 215px; height: 60px;
    background: linear-gradient(120deg, #e7c7d2, #f4eef0); }
  .photo--front { left: 822px; top: 478px; width: 226px; height: 180px;
    background: linear-gradient(150deg, #8a8a80, #b9d26a 40%, #e5a935 70%, #5a4a3a); }
</style>
</head>
<body>
  <p class="steps-kicker">How it Works</p>
  <h2 class="steps-title">EASY ORDER IN 3 STEPS</h2>

  <section class="step step--one">
    <div class="step-icon">
      <div class="step-art" role="img" aria-label="Illustration of a takeaway bag and drink cup on an orange circle"></div>
      <span class="step-number">1</span>
    </div>
    <h3 class="step-name">Explore Restaurants</h3>
    <p class="step-text">Lorem Ipsum is simply dummy text of the<br>printing and typesetting industry</p>
  </section>

  <section class="step step--two">
    <div class="step-icon">
      <div class="step-art" role="img" aria-label="Illustration of a menu card and donut on a teal circle"></div>
      <span class="step-number">2</span>
    </div>
    <h3 class="step-name">Choose a Tasty Dish</h3>
    <p class="step-text">Lorem Ipsum is simply dummy text of the<br>printing and typesetting industry</p>
  </section>

  <section class="step step--three">
    <div class="step-icon">
      <div class="step-art" role="img" aria-label="Illustration of a hand holding a phone with order tracking on a green circle"></div>
      <span class="step-number">3</span>
    </div>
    <h3 class="step-name">Follow The Status</h3>
    <p class="step-text">Lorem Ipsum is simply dummy text of the<br>printing and typesetting industry</p>
  </section>

  <h2 class="about-title">Welcome To Amber Route</h2>
  <p class="about-tag">WHO WE ARE</p>
  <p class="about-text">In publishing and graphic design, Lorem ipsum is a placeholder text commonly used to demonstrate the visual form of a document or a typeface without relying on meaningful content. Lorem ipsum may be used as a placeholder before final copy is available.</p>

  <div class="photo photo--back" role="img" aria-label="Photo of a golden potato gratin on a rustic wooden table"></div>
  <div class="photo photo--low" role="img" aria-label="Photo of a berry dessert in a glass bowl"></div>
  <div class="photo photo--front" role="img" aria-label="Photo of grilled meat with roasted plantain and green avocado sauce"></div>
</body>
</html>
```